Fast quick flyer for Merchant Showcase Fair

I am an information security consultant that needs to have a flyer and QUICK!!!
I need to get it to the printer today to have if done by monday. Quick turnaound.
I don't need the most amazing flyer but something that will capture their attention and offer them 40% off my base rate.
Updates

Here's some slight updates to the text, can you update and incorporate (PS: For some reason, when I initially put in Luvaro Systems, a " (quote) showed up, it's an apostrophe ( Luvaro Systems): Text: Luvaro Systems is the information security department for small and mid-sized businesses. Leveraging our 20+ years of information security experience, we will bring you the same level of service found at Pinnacle 400 companies. Small and mid-sized companies are often the target of malicious activity because they tend to lack the expertise to properly secure their environments. Now you can have your very own information security department at a fraction of the cost of a full time staff. Our typical rate for our premium offering: Shieldwise Direct is $5000/month based on a signed one year commitment. But for expo attendees, we are offering a special discount. As an expo attendee, you are eligible for a 40% discount. Shieldwise Direct for expo attendees will be $3000/month based on a signed one year commitment. Why put your company and your business at risk. Luvaro Systems is here to secure your company's future! Contact us now for more information: Martin Kessell Luvaro Systems "The information security department of small and mid-sized companies" 555-318-7702 info@luvarosys.example http://www.luvarosys.example

Also, this is going to be a 6x9 heavy stock postcard

Addition: Promo Code: TradeFairPass 2014

Target Market(s)

Small businesses with a small IT department that can't afford to hire a full time IT Security Staff. We are the outsourced Information Security group

Industry/Entity Type

Small Business

Colors

Designer to choose colors to be used in the design.

Requirements
Must have
• Sell the idea that they need to take security serious and that we are the ones to do the job

Should stress that because they are attendees of the Merchant Showcase Fair, they are eligible to get a 40% discount on our standard rate

```html
<!DOCTYPE html>
<html lang="en">
<head>
<meta charset="utf-8">
<title>Luvaro Systems – Expo Flyer</title>
<link rel="stylesheet" href="https://fonts.googleapis.com/css2?family=Federo&family=Roboto+Condensed:wght@300;400&display=swap">
<style>
  :root{
    --ink-dark:#141a1f;
    --ink-mid:#26313a;
    --band:rgba(20,24,28,0.82);
    --title-white:#f2f2f2;
    --title-red:#d9312b;
    --body-white:#f4f4f4;
    --offer-cyan:#2fc4d8;
    --contact-green:#2f8f7a;
    --closing-box:rgba(16,18,20,0.85);
    --closing-red:#d23a32;
  }
  *{margin:0;padding:0;box-sizing:border-box}
  html,body{width:801px;height:1200px;overflow:hidden;background:var(--ink-dark)}
  .flyer{position:relative;width:801px;height:1200px;overflow:hidden;
    background:linear-gradient(180deg,var(--ink-mid) 0%,var(--ink-dark) 100%);
    font-family:'Roboto Condensed','Arial Narrow',sans-serif;font-weight:300;color:var(--body-white)}
  .hex-backdrop{position:absolute;inset:0;
    background:
      radial-gradient(ellipse 260px 220px at 90px 330px,rgba(60,170,200,.55),transparent 70%),
      radial-gradient(ellipse 220px 200px at 300px 250px,rgba(220,180,60,.45),transparent 70%),
      radial-gradient(ellipse 200px 200px at 170px 470px,rgba(200,60,60,.4),transparent 70%),
      radial-gradient(ellipse 220px 200px at 380px 420px,rgba(90,170,90,.4),transparent 70%),
      radial-gradient(ellipse 300px 260px at 420px 780px,rgba(60,90,120,.35),transparent 70%)}
  .keyboard-photo{position:absolute;left:478px;top:122px;width:323px;height:366px;
    background:linear-gradient(160deg,#6d747b 0%,#3b4147 55%,#1c2024 100%)}
  .chip-photo{position:absolute;left:0;top:562px;width:281px;height:318px;
    background:radial-gradient(ellipse at 55% 50%,#7b7f84 0%,#3c4045 55%,transparent 80%)}
  .title-band{position:absolute;left:0;top:0;width:801px;height:96px;background:var(--band);
    display:flex;align-items:center;padding-left:22px}
  .title{font-family:'Federo',sans-serif;font-weight:400;font-size:50px;letter-spacing:1px;color:var(--title-white);white-space:nowrap}
  .title .alert{color:var(--title-red)}
  .intro{position:absolute;left:34px;top:234px;width:540px;font-size:22px;line-height:25.5px;color:var(--body-white)}
  .offer{position:absolute;left:262px;top:604px;width:530px;color:var(--offer-cyan)}
  .offer-rate{font-size:28px;line-height:34px}
  .offer-expo{margin-top:8px;font-size:23px;line-height:27px}
  .contact{position:absolute;left:559px;top:951px;width:242px;height:221px;background:var(--contact-green);
    padding:10px 0 0 20px;font-size:20px;line-height:23px;color:var(--body-white);font-style:normal}
  .contact .visit{margin-top:6px}
  .contact .promo{margin-top:6px;font-size:17px;line-height:20px;font-weight:400}
  .closing{position:absolute;left:0;top:1027px;width:506px;height:154px;background:var(--closing-box);
    font-family:'Federo',sans-serif;font-size:17px;line-height:25px;text-align:center;padding-top:14px;letter-spacing:.5px}
  .closing .risk{color:var(--closing-red)}
  .closing .promise{color:var(--body-white)}
</style>
</head>
<body>
<main class="flyer">
  <div class="hex-backdrop" role="img" aria-label="Background of overlapping translucent coloured hexagons"></div>
  <div class="keyboard-photo" role="img" aria-label="Close-up photograph of a computer keyboard"></div>
  <div class="chip-photo" role="img" aria-label="Photograph of a microchip on a circuit board"></div>

  <header class="title-band">
    <h1 class="title">STOP <span class="alert">RISKING</span> YOUR COMPANY!</h1>
  </header>

  <p class="intro">Luvaro Systems is the information security department for small and mid-sized businesses. Leveraging our 20+ years of information security experience, we will bring you the same level of service found at Pinnacle 400 companies. Small and mid-sized companies are often the target of malicious activity because they tend to lack the expertise to properly secure their environments. Now you can have your very own information security department at a fraction of the cost of a full time staff.</p>

  <section class="offer">
    <p class="offer-rate">Our typical rate for our premium offering: Shieldwise Direct is $5000/month based on a signed one year commitment. But for expo attendees, we are offering a special discount. As an expo attendee, you are eligible for a 40% discount.</p>
    <p class="offer-expo">Shieldwise Direct for expo attendees will be $3000/month based on a signed one year commitment.</p>
  </section>

  <address class="contact">
    <p>Please contact:<br>Martin Kessell<br>555-318-7702<br>info@luvarosys.example</p>
    <p class="visit">Visit us at:<br>www.luvarosys.example</p>
    <p class="promo">Promo Code:<br>TradeFairPass 2014</p>
  </address>

  <section class="closing">
    <p class="risk">WHY PUT YOUR COMPANY AND YOUR BUSINESS<br>AT RISK.</p>
    <p class="promise">LUVARO SYSTEMS IS HERE TO SECURE<br>YOUR COMPANY'S FUTURE!</p>
  </section>
</main>
</body>
</html>
```